Hoods and pressure washing

We pressure wash house, driveways, buisnesses, gas stations, restraunt hoods and equipments, fences, construction sites and anything that can be pressure washed

Will like my flyer to have written: licenesed, bonded, and insured up to 2 million.(but professionally written)

Target Market(s)

Restraunts, corporations, houses and apartment complexes

Industry/Entity Type

Construction

Colors
33a6d7
33b8a4
ffffff
3176b5

Requirements
Must have
• Before and after pics of dirty and clean pics
Nice to have
• I would like it to be a one paper flyer could be front or back. Company name is aquaBrite. I like a corner written down with all the work we do. Ex: hoods, sidewalks, sidings, houses etc...
• Contact info: Dennis Cawley, phone# 629-415-3307
• Lou Marten, phone # (didnt get one yet)
• Adress: 2417 E. Brantwood rd, portland, Tn, 37162

```html
<!DOCTYPE html>
<html lang="en">
<head>
<meta charset="utf-8">
<title>aquaBrite Pressure Washing Flyer</title>
<link rel="stylesheet" href="https://fonts.googleapis.com/css2?family=Open+Sans:wght@400;600;700&family=Roboto+Condensed:wght@700&display=swap">
<style>
  :root {
    --blue: #1f8fd0;
    --blue-light: #33b4e6;
    --blue-dark: #0d5f9a;
    --ink: #2b2b2b;
    --footer: #1b1b1d;
    --white: #ffffff;
  }
  * { margin: 0; padding: 0; box-sizing: border-box; }
  html, body { width: 971px; height: 1200px; overflow: hidden; background: #fff; }
  .flyer {
    position: relative; width: 971px; height: 1200px; overflow: hidden;
    background: var(--white); font-family: "Open Sans", sans-serif; color: var(--ink);
  }
  .hero-photo {
    position: absolute; left: 0; top: 0; width: 971px; height: 640px;
    background: linear-gradient(180deg, #d9dde2 0%, #eef0f2 40%, #c9ccc6 62%, #4f8a3a 78%, #5a9442 100%);
  }
  .shapes { position: absolute; inset: 0; }
  .brand {
    position: absolute; right: 26px; top: 44px;
    display: flex; flex-direction: column; align-items: flex-end; gap: 8px;
  }
  .brand-mark { display: flex; align-items: center; gap: 12px; }
  .brand-dot { width: 30px; height: 30px; border-radius: 50%; background: var(--blue); flex: none; }
  .brand-name {
    font-weight: 700; font-size: 42px; color: var(--ink);
    text-transform: uppercase; line-height: 1; white-space: nowrap;
  }
  .brand-credentials {
    font-weight: 600; font-size: 16px; color: var(--blue-dark); white-space: nowrap;
  }
  .sample {
    position: absolute; border-radius: 50%; border: 6px solid var(--white);
    box-shadow: 0 0 0 5px var(--blue), 0 6px 12px rgba(0,0,0,.35);
  }
  .sample-paving { left: 332px; top: 455px; width: 150px; height: 150px;
    background: linear-gradient(100deg, #a86a62 0%, #9a6a62 45%, #6f6e68 55%, #585a55 100%); }
  .sample-deck { left: 564px; top: 428px; width: 170px; height: 170px;
    background: linear-gradient(135deg, #8a7a62 0%, #b59a72 50%, #6c5e4b 100%); }
  .sample-siding { left: 792px; top: 390px; width: 176px; height: 176px;
    background: linear-gradient(160deg, #9fb7c8 0%, #c4d4de 50%, #7f98aa 100%); }
  .section-tab {
    position: absolute; left: 0; top: 632px; width: 452px; height: 60px;
    background: linear-gradient(90deg, var(--blue-light), var(--blue-dark));
    border-radius: 0 14px 14px 0; box-shadow: 0 4px 8px rgba(0,0,0,.3);
    color: var(--white); font-weight: 600; font-size: 33px; line-height: 60px; padding-left: 38px;
  }
  .intro {
    position: absolute; left: 32px; top: 708px; width: 920px;
    font-size: 26px; line-height: 34px; color: #222; white-space: nowrap;
  }
  .services { position: absolute; left: 30px; top: 794px; list-style: none; }
  .services li {
    display: flex; align-items: center; height: 42px;
    font-weight: 700; font-size: 30px; color: #3a3a3a;
  }
  .services svg { width: 32px; height: 32px; margin-right: 34px; }
  .price-badge { position: absolute; left: 590px; top: 795px; width: 300px; height: 300px; }
  .price-label {
    position: absolute; left: 590px; top: 876px; width: 300px; text-align: center;
    font-family: "Roboto Condensed", sans-serif; font-weight: 700; font-size: 28px; color: var(--white);
  }
  .price-value {
    position: absolute; left: 590px; top: 905px; width: 300px; text-align: center;
    font-family: "Roboto Condensed", sans-serif; font-weight: 700; font-size: 84px; color: var(--white); line-height: 1.05;
  }
  .contact-bar {
    position: absolute; left: 0; top: 1120px; width: 971px; height: 80px;
    background: linear-gradient(180deg, #3a3a3d, var(--footer));
    border-top: 5px solid var(--blue);
  }
  .contact { position: absolute; top: 14px; display: flex; align-items: center; gap: 12px;
    color: var(--white); font-weight: 600; font-size: 19px; line-height: 25px; white-space: nowrap; }
  .contact-icon { width: 38px; height: 38px; border-radius: 50%; background: var(--blue);
    display: flex; align-items: center; justify-content: center; flex: none; }
  .contact-icon svg { width: 22px; height: 22px; fill: #fff; }
  .contact-address { left: 40px; }
  .contact-primary { left: 415px; }
  .contact-secondary { left: 730px; }
</style>
</head>
<body>
<div class="flyer">
  <div class="hero-photo" role="img" aria-label="Worker pressure washing the front of a two-storey house with lawn and garage"></div>

  <svg class="shapes" width="971" height="1200" viewBox="0 0 971 1200" aria-hidden="true">
    <defs>
      <linearGradient id="swoosh" x1="0" x2="1">
        <stop offset="0" stop-color="#1a7fc4"/>
        <stop offset="1" stop-color="#35b8ea"/>
      </linearGradient>
      <linearGradient id="softGrey" x1="0" y1="0" x2="0" y2="1">
        <stop offset="0" stop-color="#ffffff"/>
        <stop offset="1" stop-color="#dcdcdf"/>
      </linearGradient>
    </defs>
    <path d="M330 0 Q560 190 971 270 L971 300 Q540 250 300 0 Z" fill="url(#swoosh)"/>
    <path d="M350 0 Q590 175 971 250 L971 262 Q575 190 335 0 Z" fill="#7fd0f2"/>
    <path d="M355 0 Q600 160 971 238 L971 0 Z" fill="#fff"/>
    <path d="M0 470 Q420 620 971 500 L971 560 Q420 660 0 530 Z" fill="url(#swoosh)"/>
    <path d="M0 520 Q420 640 971 545 L971 1200 L0 1200 Z" fill="#fff"/>
    <path d="M0 515 Q420 632 971 540" fill="none" stroke="#7fd0f2" stroke-width="6"/>
    <path d="M0 850 Q40 1070 330 1116 L0 1116 Z" fill="url(#softGrey)"/>
  </svg>

  <div class="brand">
    <div class="brand-mark">
      <span class="brand-dot"></span>
      <span class="brand-name">aquaBrite</span>
    </div>
    <p class="brand-credentials">Licensed, Bonded &amp; Insured up to $2 Million</p>
  </div>

  <div class="sample sample-paving" role="img" aria-label="Paving bricks half dirty, half cleaned"></div>
  <div class="sample sample-deck" role="img" aria-label="Wooden deck boards being pressure washed"></div>
  <div class="sample sample-siding" role="img" aria-label="Clean house siding panels"></div>

  <div class="section-tab">PRESSURE WASHING</div>

  <p class="intro">We pressure wash house, driveways, buisnesses, gas stations,<br>restraunt hoods and equipments, fences, construction sites...</p>

  <ul class="services">
    <li><svg viewBox="0 0 32 32"><circle cx="16" cy="16" r="15" fill="var(--blue)"/><path d="M9 16.5l5 5 9-10" fill="none" stroke="#fff" stroke-width="3.5" stroke-linecap="round" stroke-linejoin="round"/></svg>Fleet Washes</li>
    <li><svg viewBox="0 0 32 32"><circle cx="16" cy="16" r="15" fill="var(--blue)"/><path d="M9 16.5l5 5 9-10" fill="none" stroke="#fff" stroke-width="3.5" stroke-linecap="round" stroke-linejoin="round"/></svg>Whole Homes</li>
    <li><svg viewBox="0 0 32 32"><circle cx="16" cy="16" r="15" fill="var(--blue)"/><path d="M9 16.5l5 5 9-10" fill="none" stroke="#fff" stroke-width="3.5" stroke-linecap="round" stroke-linejoin="round"/></svg>Hoods</li>
    <li><svg viewBox="0 0 32 32"><circle cx="16" cy="16" r="15" fill="var(--blue)"/><path d="M9 16.5l5 5 9-10" fill="none" stroke="#fff" stroke-width="3.5" stroke-linecap="round" stroke-linejoin="round"/></svg>Drive Thrus</li>
    <li><svg viewBox="0 0 32 32"><circle cx="16" cy="16" r="15" fill="var(--blue)"/><path d="M9 16.5l5 5 9-10" fill="none" stroke="#fff" stroke-width="3.5" stroke-linecap="round" stroke-linejoin="round"/></svg>Commercial Building</li>
    <li><svg viewBox="0 0 32 32"><circle cx="16" cy="16" r="15" fill="var(--blue)"/><path d="M9 16.5l5 5 9-10" fill="none" stroke="#fff" stroke-width="3.5" stroke-linecap="round" stroke-linejoin="round"/></svg>Sidewalks</li>
    <li><svg viewBox="0 0 32 32"><circle cx="16" cy="16" r="15" fill="var(--blue)"/><path d="M9 16.5l5 5 9-10" fill="none" stroke="#fff" stroke-width="3.5" stroke-linecap="round" stroke-linejoin="round"/></svg>Much More!</li>
  </ul>

  <svg class="price-badge" viewBox="0 0 300 300" aria-hidden="true">
    <defs>
      <linearGradient id="badgeFill" x1="0" y1="0" x2="1" y2="1">
        <stop offset="0" stop-color="#37b9ec"/>
        <stop offset="1" stop-color="#0d5f9a"/>
      </linearGradient>
      <radialGradient id="badgeShadow"><stop offset="0" stop-color="rgba(0,0,0,.25)"/><stop offset="1" stop-color="rgba(0,0,0,0)"/></radialGradient>
    </defs>
    <ellipse cx="150" cy="282" rx="120" ry="12" fill="url(#badgeShadow)"/>
    <polygon fill="url(#badgeFill)" points="150,10 164,28 182,14 192,35 213,26 218,49 240,46 239,69 261,73 253,94 274,104 260,122 278,137 260,150 278,163 260,178 274,196 253,206 261,227 239,231 240,254 218,251 213,274 192,265 182,286 164,272 150,290 136,272 118,286 108,265 87,274 82,251 60,254 61,231 39,227 47,206 26,196 40,178 22,163 40,150 22,137 40,122 26,104 47,94 39,73 61,69 60,46 82,49 87,26 108,35 118,14 136,28"/>
  </svg>
  <div class="price-label">Prices start at:</div>
  <div class="price-value">$49.99</div>

  <footer class="contact-bar">
    <div class="contact contact-address">
      <span class="contact-icon"><svg viewBox="0 0 24 24"><path d="M12 3l9 8h-3v9h-4v-6h-4v6H6v-9H3z"/></svg></span>
      <span>2417 E. Brantwood rd,<br>Portland, Tn, 37162</span>
    </div>
    <div class="contact contact-primary">
      <span class="contact-icon"><svg viewBox="0 0 24 24"><path d="M6.6 10.8a15 15 0 006.6 6.6l2.2-2.2a1 1 0 011-.25 11.4 11.4 0 003.6.57 1 1 0 011 1V20a1 1 0 01-1 1A17 17 0 013 4a1 1 0 011-1h3.5a1 1 0 011 1c0 1.25.2 2.45.57 3.57a1 1 0 01-.25 1z"/></svg></span>
      <span>Dennis Cawley<br>629-415-3307</span>
    </div>
    <div class="contact contact-secondary">
      <span class="contact-icon"><svg viewBox="0 0 24 24"><path d="M6.6 10.8a15 15 0 006.6 6.6l2.2-2.2a1 1 0 011-.25 11.4 11.4 0 003.6.57 1 1 0 011 1V20a1 1 0 01-1 1A17 17 0 013 4a1 1 0 011-1h3.5a1 1 0 011 1c0 1.25.2 2.45.57 3.57a1 1 0 01-.25 1z"/></svg></span>
      <span>Lou Marten<br>629-415-3307</span>
    </div>
  </footer>
</div>
</body>
</html>
```